The Harbourlight CV consultant

The service is premium. It is aimed at people 18-30, so students and those looking to change their first job, principally in the UK but also global. It is offering a very personalised CV writing service and is much more expensive than others on offer. I am very keen that it should look simple and premium. It needs to look very professional, reflecting the aspirational jobs that the clients will be applying for.
If there were three words that summed it up: modern, clean, premium.
I am waiting for all the testimonials to come in but they need to form a major part of the website.
I am also waiting for the full logo design files so that I can upload them. In the meantime there is a copy of the logo.
Thoughts to help those yet to send a design...
This is a premium service and some of the designs have looked very generic. The focus needs to be on quality and the process mentioned in the brief. The partnership and the advantages it brings are crucial but few have mentioned that.

```html
<!DOCTYPE html>
<html lang="en">
<head>
<meta charset="utf-8">
<title>The Harbourlight CV Consultant</title>
<link href="https://fonts.googleapis.com/css2?family=Cinzel:wght@600;700&family=Outfit:wght@300;400;500;600&display=swap" rel="stylesheet">
<style>
:root{
  --blue:#1b6ec2;
  --blue-dark:#135aa3;
  --ink:#1d1d1d;
  --muted:#555;
  --grey-bg:#f4f4f4;
  --line:#e3e3e3;
  --white:#fff;
  --star:#e2574c;
}
*{box-sizing:border-box;margin:0;padding:0}
html,body{width:1200px;height:4938px;overflow:hidden}
body{font-family:"Outfit",sans-serif;color:var(--ink);background:var(--white);position:relative}
.serif{font-family:"Cinzel",serif}
.btn{display:inline-block;background:var(--blue);color:var(--white);font-weight:600;font-size:15px;letter-spacing:.3px;border-radius:22px;padding:12px 28px}
.section{position:absolute;left:0;width:1200px}
.section-title{font-family:"Cinzel",serif;font-weight:700;font-size:36px;text-align:center;line-height:1.2}
.section-title::after{content:"";display:block;width:60px;height:3px;background:var(--blue);margin:12px auto 0}

/* top bar */
.topbar{top:0;height:31px;background:var(--blue);color:var(--white);font-size:12px;display:flex;justify-content:flex-end;align-items:center;gap:22px;padding-right:110px}
.topbar .item{display:flex;align-items:center;gap:6px}
.topbar .socials{display:flex;gap:12px;border-left:1px solid rgba(255,255,255,.5);padding-left:14px}
.topbar .socials span{width:11px;height:11px;border-radius:50%;background:var(--white);display:block}

/* nav */
.nav{top:31px;height:61px;display:flex;align-items:center;justify-content:space-between;padding:0 100px}
.brand{display:flex;align-items:center;gap:10px;color:var(--blue)}
.brand-mark{width:14px;height:14px;border-radius:50%;background:var(--blue)}
.brand-name{font-family:"Outfit",sans-serif;font-weight:500;font-size:15px;color:var(--blue)}
.menu{display:flex;gap:36px;font-size:13px;font-weight:500}

/* hero */
.hero{top:92px;height:627px;background:linear-gradient(100deg,#3e5a6d 0%,#7e96a3 35%,#c9d3d8 60%,#aab6bd 100%)}
.hero-text{position:absolute;left:100px;top:225px;color:var(--white)}
.hero-text h1{font-family:"Cinzel",serif;font-weight:600;font-size:29px;line-height:1.25;width:420px;margin-bottom:22px}

/* about */
.about{top:719px;height:517px}
.about-frame{position:absolute;left:98px;top:66px;width:498px;height:376px;border-left:6px solid var(--blue);border-top:6px solid var(--blue)}
.about-photo{position:absolute;left:106px;top:74px;width:494px;height:370px;background:linear-gradient(120deg,#c7b39b,#e9e2d8 50%,#8fa9c4)}
.about-copy{position:absolute;left:652px;top:72px;width:448px}
.about-copy h2{font-family:"Cinzel",serif;font-weight:700;font-size:36px;line-height:1.12;margin-bottom:26px}
.about-copy p{font-size:14px;line-height:1.7;color:var(--muted);text-align:justify;margin-bottom:12px}
.about-copy .btn{margin-top:14px}

/* how it works */
.how{top:1236px;height:466px;background:var(--grey-bg)}
.how .section-title{margin-top:62px}
.steps{position:absolute;top:164px;left:100px;width:1000px;display:flex}
.step{width:250px;text-align:center}
.step-icon{position:relative;width:111px;height:111px;margin:0 auto 20px;border:1.5px solid #9fc1e5;border-radius:50%;background:var(--white);display:flex;align-items:center;justify-content:center}
.step-num{position:absolute;right:-4px;top:-4px;width:32px;height:32px;border-radius:50%;background:var(--blue);color:var(--white);font-size:13px;font-weight:600;display:flex;align-items:center;justify-content:center;border:3px solid var(--grey-bg)}
.step h3{font-size:17px;font-weight:500;margin-bottom:10px}
.step p{font-size:12.5px;line-height:1.6;color:var(--muted);padding:0 6px}

/* packages */
.packages{top:1702px;height:1074px}
.packages .section-title{margin-top:80px}
.pkg-grid{position:absolute;left:100px;top:161px;width:1000px;display:grid;grid-template-columns:repeat(3,314px);column-gap:29px;row-gap:25px}
.pkg{height:399px;background:var(--white);box-shadow:0 0 8px rgba(0,0,0,.12);text-align:center}
.pkg-head{height:76px;background:var(--blue);color:var(--white);font-weight:600;font-size:20px;line-height:1.2;display:flex;align-items:center;justify-content:center;border-bottom:3px solid var(--blue-dark)}
.pkg-roles{font-size:12px;line-height:1.35;margin:16px 16px 8px;color:#333}
.pkg-price{font-size:27px;font-weight:600;color:var(--blue);margin-bottom:12px}
.pkg p{font-size:11.6px;line-height:1.72;color:var(--muted);text-align:justify;text-align-last:center;padding:0 20px;margin-bottom:16px}
.pkg .btn{font-size:14px;padding:11px 28px}

/* benefits */
.benefits{top:2776px;height:742px;background:var(--grey-bg)}
.benefits .section-title{margin-top:94px}
.ben-frame{position:absolute;left:115px;top:196px;width:444px;height:460px;background:var(--blue)}
.ben-photo{position:absolute;left:127px;top:210px;width:442px;height:456px;background:linear-gradient(135deg,#3e4a5c,#7c8fa8 40%,#c9cfd8 70%,#6c7480)}
.ben-list{position:absolute;left:636px;top:258px;width:460px;list-style:none}
.ben-list li{position:relative;padding-left:37px;margin-bottom:30px}
.ben-list svg{position:absolute;left:0;top:2px}
.ben-list h3{font-size:18px;font-weight:500;margin-bottom:6px}
.ben-list p{font-size:12.5px;line-height:1.75;color:var(--muted)}

/* testimonials */
.testimonials{top:3518px;height:485px}
.testimonials .section-title{margin-top:70px}
.t-grid{position:absolute;left:100px;top:143px;width:1000px;display:grid;grid-template-columns:repeat(3,314px);column-gap:29px}
.t-card{height:259px;background:var(--white);box-shadow:0 0 8px rgba(0,0,0,.12);padding:18px 20px}
.t-head{display:flex;align-items:center;gap:14px;margin-bottom:16px}
.avatar{width:42px;height:42px;border-radius:50%;background:#c9d1da}
.t-name{font-size:15px;font-weight:500}
.t-card p{font-style:italic;font-size:14.5px;line-height:1.75;color:#444;text-align:justify;margin-bottom:8px}
.stars{color:var(--star);font-size:20px;letter-spacing:1px}

/* faq */
.faq{top:4003px;height:607px;background:var(--grey-bg)}
.faq .section-title{margin-top:84px}
.faq-list{position:absolute;left:226px;top:144px;width:748px}
.faq-item{background:var(--white);margin-bottom:18px;height:46px;padding:0 20px;display:flex;align-items:center;justify-content:space-between;font-size:13px;font-weight:600}
.faq-item.open{height:124px;display:block;padding:14px 20px}
.faq-item.open .q{display:flex;justify-content:space-between;margin-bottom:14px}
.faq-item.open p{font-weight:400;font-size:11px;line-height:1.9;color:var(--muted)}
.caret{width:0;height:0;border-left:6px solid transparent;border-right:6px solid transparent;border-top:7px solid var(--ink)}

/* footer */
.footer{top:4610px;height:328px;background:var(--blue);color:var(--white)}
.f-brand{position:absolute;left:103px;top:66px;display:flex;align-items:center;gap:10px}
.f-brand .brand-mark{background:var(--white)}
.f-brand .brand-name{color:var(--white);font-size:17px}
.f-socials{position:absolute;left:118px;top:167px;display:flex;gap:18px}
.f-socials span{width:36px;height:36px;border-radius:50%;background:var(--white);display:block}
.f-col{position:absolute;top:58px}
.f-col h4{font-size:19px;font-weight:500;margin-bottom:14px}
.f-col ul{list-style:none;font-size:13px;line-height:2.35}
.f-col address{font-style:normal;font-size:13px;line-height:1.7}
.copyright{position:absolute;left:100px;top:272px;width:1000px;border-top:1px solid rgba(255,255,255,.45);text-align:center;font-size:14px;padding-top:12px}
</style>
</head>
<body>

<div class="section topbar">
  <div class="item">
    <svg width="12" height="12" viewBox="0 0 24 24"><path fill="#fff" d="M6.6 10.8a15 15 0 0 0 6.6 6.6l2.2-2.2a1 1 0 0 1 1-.25 11.4 11.4 0 0 0 3.6.57 1 1 0 0 1 1 1V20a1 1 0 0 1-1 1A17 17 0 0 1 3 4a1 1 0 0 1 1-1h3.5a1 1 0 0 1 1 1c0 1.25.2 2.45.57 3.57a1 1 0 0 1-.25 1z"/></svg>
    Call Us: +1 555 -010 -4821
  </div>
  <div class="item">
    <svg width="14" height="11" viewBox="0 0 24 18"><rect x="1" y="1" width="22" height="16" fill="none" stroke="#fff" stroke-width="2"/><path d="M1 1l11 9 11-9" fill="none" stroke="#fff" stroke-width="2"/></svg>
    Email Us: harbourlightcvconsultant.com
  </div>
  <div class="socials"><span></span><span></span><span></span><span></span></div>
</div>

<header class="section nav">
  <div class="brand"><span class="brand-mark"></span><span class="brand-name">The Harbourlight CV Consultant</span></div>
  <nav class="menu"><span>HOME</span><span>SERVICES</span><span>FREE CV REVIEW</span><span>MEET YOUR COACH</span><span>BLOG</span><span>CONTACT US</span></nav>
</header>

<section class="section hero" role="img" aria-label="Photo of two professionals in an office reviewing a tablet together">
  <div class="hero-text">
    <h1>Showcase your career bests with our resume-writing services</h1>
    <span class="btn">BOOK A CONSULTATION</span>
  </div>
</section>

<section class="section about">
  <div class="about-frame"></div>
  <div class="about-photo" role="img" aria-label="Photo of hands holding printed CVs on a desk"></div>
  <div class="about-copy">
    <h2>The Harbourlight CV Consultant</h2>
    <p>Sed ut perspiciatis unde omnis iste natus error sit voluptatem accusantium doloremque laudantium, totam rem aperiam, eaque ipsa quae ab illo inventore veritatis et quasi architecto beatae vitae dicta sunt explicabo. Nemo enim ipsam voluptatem quia voluptas sit aspernatur aut odit</p>
    <p>Sed ut perspiciatis unde omnis iste natus error sit voluptatem accusantium doloremque laudantium,</p>
    <span class="btn">LEARN MORE</span>
  </div>
</section>

<section class="section how">
  <h2 class="section-title">Let's see how it works</h2>
  <div class="steps">
    <div class="step">
      <div class="step-icon"><span class="step-num">01</span>
        <svg width="40" height="44" viewBox="0 0 40 44" fill="none" stroke="#1b6ec2" stroke-width="2"><rect x="4" y="2" width="32" height="40" rx="2"/><rect x="10" y="9" width="10" height="10"/><path d="M24 11h7M24 16h7M10 25h21M10 30h21M10 35h15"/></svg>
      </div>
      <h3>Resume Packages</h3>
      <p>Lorem ipsum dolor sit amet, csectetur adipiscing elit, sed do usmod tempor incididunt ut labore et</p>
    </div>
    <div class="step">
      <div class="step-icon"><span class="step-num">02</span>
        <svg width="44" height="40" viewBox="0 0 44 40" fill="none" stroke="#1b6ec2" stroke-width="2"><path d="M3 16l19-13 19 13v21H3z"/><path d="M3 16l19 13 19-13"/><circle cx="22" cy="15" r="5"/></svg>
      </div>
      <h3>Answer via email</h3>
      <p>Lorem ipsum dolor sit amet, csectetur adipiscing elit, sed do usmod tempor incididunt ut labore et</p>
    </div>
    <div class="step">
      <div class="step-icon"><span class="step-num">03</span>
        <svg width="46" height="40" viewBox="0 0 46 40" fill="none" stroke="#1b6ec2" stroke-width="2"><circle cx="10" cy="9" r="4"/><circle cx="23" cy="9" r="4"/><circle cx="36" cy="9" r="4"/><path d="M4 38V22a6 6 0 0 1 12 0v16M17 38V22a6 6 0 0 1 12 0v16M30 38V22a6 6 0 0 1 12 0v16M2 30h42"/></svg>
      </div>
      <h3>Consultation</h3>
      <p>Lorem ipsum dolor sit amet, csectetur adipiscing elit, sed do usmod tempor incididunt ut labore et</p>
    </div>
    <div class="step">
      <div class="step-icon"><span class="step-num">04</span>
        <svg width="40" height="44" viewBox="0 0 40 44" fill="none" stroke="#1b6ec2" stroke-width="2"><rect x="3" y="3" width="34" height="38" rx="2"/><rect x="9" y="9" width="10" height="10"/><path d="M23 11h8M23 16h8M9 25h22M9 30h22M9 35h12"/></svg>
      </div>
      <h3>Get Resume</h3>
      <p>Lorem ipsum dolor sit amet, csectetur adipiscing elit, sed do usmod tempor incididunt ut labore et</p>
    </div>
  </div>
</section>

<section class="section packages">
  <h2 class="section-title">Our Packages</h2>
  <div class="pkg-grid">
    <article class="pkg"><div class="pkg-head">Executive CV +<br>Cover Letter</div><div class="pkg-roles">PROJECT MANAGERS, BUSINESS ANALYSTS, DEVELOPERS, TESTERS</div><div class="pkg-price">£225.00</div><p>Your CV is your first opportunity to make an impression on employers. It's important to show off your skills, experience, and accomplishments so you can stand out from other applicants. Your CV will also help demonstrate your value to a company and convince them that you are the right person for the job.</p><span class="btn">GET STARTED</span></article>
    <article class="pkg"><div class="pkg-head">Management CV +<br>Cover Letter</div><div class="pkg-roles">PROJECT MANAGERS, BUSINESS ANALYSTS, DEVELOPERS, TESTERS</div><div class="pkg-price">£225.00</div><p>Your CV is your first opportunity to make an impression on employers. It's important to show off your skills, experience, and accomplishments so you can stand out from other applicants. Your CV will also help demonstrate your value to a company and convince them that you are the right person for the job.</p><span class="btn">GET STARTED</span></article>
    <article class="pkg"><div class="pkg-head">Professional CV +<br>Cover Letter</div><div class="pkg-roles">PROJECT MANAGERS, BUSINESS ANALYSTS, DEVELOPERS, TESTERS</div><div class="pkg-price">£225.00</div><p>Your CV is your first opportunity to make an impression on employers. It's important to show off your skills, experience, and accomplishments so you can stand out from other applicants. Your CV will also help demonstrate your value to a company and convince them that you are the right person for the job.</p><span class="btn">GET STARTED</span></article>
    <article class="pkg"><div class="pkg-head">Technical CV +<br>Cover Letter</div><div class="pkg-roles">PROJECT MANAGERS, BUSINESS ANALYSTS, DEVELOPERS, TESTERS</div><div class="pkg-price">£225.00</div><p>Your CV is your first opportunity to make an impression on employers. It's important to show off your skills, experience, and accomplishments so you can stand out from other applicants. Your CV will also help demonstrate your value to a company and convince them that you are the right person for the job.</p><span class="btn">GET STARTED</span></article>
    <article class="pkg"><div class="pkg-head">Graduate CV +<br>Cover Letter</div><div class="pkg-roles">PROJECT MANAGERS, BUSINESS ANALYSTS, DEVELOPERS, TESTERS</div><div class="pkg-price">£225.00</div><p>Your CV is your first opportunity to make an impression on employers. It's important to show off your skills, experience, and accomplishments so you can stand out from other applicants. Your CV will also help demonstrate your value to a company and convince them that you are the right person for the job.</p><span class="btn">GET STARTED</span></article>
    <article class="pkg"><div class="pkg-head">TECH DIY CVs +<br>Cover Letters</div><div class="pkg-roles">PROJECT MANAGERS, BUSINESS ANALYSTS, DEVELOPERS, TESTERS</div><div class="pkg-price">£225.00</div><p>Your CV is your first opportunity to make an impression on employers. It's important to show off your skills, experience, and accomplishments so you can stand out from other applicants. Your CV will also help demonstrate your value to a company and convince them that you are the right person for the job.</p><span class="btn">GET STARTED</span></article>
  </div>
</section>

<section class="section benefits">
  <h2 class="section-title">4 Benefits of a professionally<br>written resume</h2>
  <div class="ben-frame"></div>
  <div class="ben-photo" role="img" aria-label="Photo of a coach presenting a resume on a screen to a client"></div>
  <ul class="ben-list">
    <li><svg width="24" height="24" viewBox="0 0 24 24"><circle cx="12" cy="12" r="12" fill="#1b6ec2"/><path d="M6.5 12.5l3.5 3.5 7.5-8" fill="none" stroke="#fff" stroke-width="2.4"/></svg><h3>5x-10x more interview calls</h3><p>Sed ut perspiciatis unde omnis iste natus error sit voluptausantium doloremque laudantium, totam rem aperiam</p></li>
    <li><svg width="24" height="24" viewBox="0 0 24 24"><circle cx="12" cy="12" r="12" fill="#1b6ec2"/><path d="M6.5 12.5l3.5 3.5 7.5-8" fill="none" stroke="#fff" stroke-width="2.4"/></svg><h3>5x-10x more interview calls</h3><p>Sed ut perspiciatis unde omnis iste natus error sit voluptausantium doloremque laudantium, totam rem aperiam</p></li>
    <li><svg width="24" height="24" viewBox="0 0 24 24"><circle cx="12" cy="12" r="12" fill="#1b6ec2"/><path d="M6.5 12.5l3.5 3.5 7.5-8" fill="none" stroke="#fff" stroke-width="2.4"/></svg><h3>5x-10x more interview calls</h3><p>Sed ut perspiciatis unde omnis iste natus error sit voluptausantium doloremque laudantium, totam rem aperiam</p></li>
    <li><svg width="24" height="24" viewBox="0 0 24 24"><circle cx="12" cy="12" r="12" fill="#1b6ec2"/><path d="M6.5 12.5l3.5 3.5 7.5-8" fill="none" stroke="#fff" stroke-width="2.4"/></svg><h3>5x-10x more interview calls</h3><p>Sed ut perspiciatis unde omnis iste natus error sit voluptausantium doloremque laudantium, totam rem aperiam</p></li>
  </ul>
</section>

<section class="section testimonials">
  <h2 class="section-title">Testimonial</h2>
  <div class="t-grid">
    <article class="t-card"><div class="t-head"><span class="avatar" role="img" aria-label="Client portrait"></span><span class="t-name">Daniel Hart</span></div><p>Lorem ipsum dolor sit amet, consectetur adipiscing elit, sed do eiusmod tempor incididunt ut labore et dolore magna aliqua. Ut enim ad minim veniam, quis nostrud exercitation ullamco</p><div class="stars">★★★★★</div></article>
    <article class="t-card"><div class="t-head"><span class="avatar" role="img" aria-label="Client portrait"></span><span class="t-name">Daniel Hart</span></div><p>Lorem ipsum dolor sit amet, consectetur adipiscing elit, sed do eiusmod tempor incididunt ut labore et dolore magna aliqua. Ut enim ad minim veniam, quis nostrud exercitation ullamco</p><div class="stars">★★★★★</div></article>
    <article class="t-card"><div class="t-head"><span class="avatar" role="img" aria-label="Client portrait"></span><span class="t-name">Daniel Hart</span></div><p>Lorem ipsum dolor sit amet, consectetur adipiscing elit, sed do eiusmod tempor incididunt ut labore et dolore magna aliqua. Ut enim ad minim veniam, quis nostrud exercitation ullamco</p><div class="stars">★★★★★</div></article>
  </div>
</section>

<section class="section faq">
  <h2 class="section-title">Frequently asked questions</h2>
  <div class="faq-list">
    <div class="faq-item open"><div class="q"><span>Lorem ipsum dolor sit amet, consectetur adipisci sed do eiusmod</span><span class="caret"></span></div><p>Lorem ipsum dolor sit amet, consectetur adipiscing elit, sed do eiusmod tempor incididunt ut labore et dolore magna aliqua. Quis ipsum suspendisse ultrices gravida. Risus commodo viverra maecenas accumsan lacus vel facilisis. Lorem ipsum dolor sit amet, consectetur adipiscing elit, sed do</p></div>
    <div class="faq-item"><span>Lorem ipsum dolor sit amet, consectetur adipisci sed do eiusmod</span><span class="caret"></span></div>
    <div class="faq-item"><span>Lorem ipsum dolor sit amet, consectetur adipisci sed do eiusmod</span><span class="caret"></span></div>
    <div class="faq-item"><span>Lorem ipsum dolor sit amet, consectetur adipisci sed do eiusmod</span><span class="caret"></span></div>
    <div class="faq-item"><span>Lorem ipsum dolor sit amet, consectetur adipisci sed do eiusmod</span><span class="caret"></span></div>
  </div>
</section>

<footer class="section footer">
  <div class="f-brand"><span class="brand-mark"></span><span class="brand-name">The Harbourlight<br>CV Consultant</span></div>
  <div class="f-socials"><span></span><span></span><span></span><span></span></div>
  <div class="f-col" style="left:439px"><h4>Quick Links</h4><ul><li>Home</li><li>Services</li><li>Free CV Review</li><li>Meet Your Coach</li><li>Blog</li><li>Contact Us</li></ul></div>
  <div class="f-col" style="left:680px"><h4>Other Links</h4><ul><li>Contact Sales</li><li>Legal Hub</li><li>Privacy Policy</li><li>Trust &amp; Security</li><li>Cookie Preferences</li></ul></div>
  <div class="f-col" style="left:917px"><h4>Contact Info</h4><address>48 Quay Street<br>Portside, UK 10482<br><span style="display:block;margin-top:8px">+1 555 - 010 - 4821</span><span style="display:block;margin-top:14px;font-weight:500">harbourlightcvconsultant.com</span></address></div>
  <div class="copyright">©Copyright 2024 The Harbourlight CV consultant. All Rights Reserved.</div>
</footer>

</body>
</html>
```